Home builder/contractor needs business presentation brochure

We are a custom home and remodeling firm who would like a great brochure to present to architects, designers, real estate brokers.

We are looking for additional avenues for growth potential and the ability to partner with the above types of businesses to give us an all around encompassing one stop shopping.

Target Market(s)

architects, designers, real estate brokers.

Industry/Entity Type

Real Estate

Requirements
Must have
• Please make this a tri fold and please checkout my website mesaridgehomes.example and my houzz site as well as yelp. to gather additional information.

```html
<!DOCTYPE html>
<html lang="en">
<head>
<meta charset="utf-8">
<title>Brochure Inside Spread</title>
<link rel="stylesheet" href="https://fonts.googleapis.com/css2?family=Cinzel:wght@600;700&family=Encode+Sans+Condensed:wght@400&family=Play&display=swap">
<style>
  :root {
    --board: #4b4e53;
    --board-dark: #3f4247;
    --sheet-top: #f6f7f8;
    --sheet-bottom: #e4e6e8;
    --band: #6aaede;
    --heading: #4d86b5;
    --body-text: #505357;
    --rule: #b9bdc1;
    --white: #ffffff;
  }
  * { margin: 0; padding: 0; box-sizing: border-box; }
  html, body { width: 1200px; height: 1000px; overflow: hidden; }
  body {
    position: relative;
    background: radial-gradient(ellipse at 50% 40%, var(--board) 0%, var(--board-dark) 100%);
  }
  .board-label {
    position: absolute; left: 24px; top: 30px;
    font-family: "Play", sans-serif; font-size: 29px; color: var(--white);
  }
  .spread {
    position: absolute; left: 22px; top: 74px; width: 1156px; height: 894px;
    background: linear-gradient(180deg, var(--sheet-top), var(--sheet-bottom));
    box-shadow: 0 4px 14px rgba(0,0,0,.45);
  }
  .photo { position: absolute; }
  .photo--villa { left: 0; top: 0; width: 586px; height: 278px;
    background: linear-gradient(180deg, #eef0f0 0%, #8b6e55 40%, #6b4e36 70%, #4e5a3c 100%); }
  .photo--pergola { left: 591px; top: 0; width: 319px; height: 211px;
    background: linear-gradient(180deg, #6f4a30 0%, #a79c8e 45%, #c8b9a6 100%); }
  .photo--shower { left: 915px; top: 0; width: 241px; height: 312px;
    background: linear-gradient(135deg, #d8cdb9 0%, #c9b89e 55%, #e7e1d6 100%); }
  .photo--cherry-kitchen { left: 0; top: 280px; width: 311px; height: 226px;
    background: linear-gradient(180deg, #d9d2c8 0%, #7a4330 40%, #5a2e20 100%); }
  .photo--white-kitchen { left: 314px; top: 280px; width: 272px; height: 226px;
    background: linear-gradient(180deg, #f1efec 0%, #cfc8be 50%, #9b9894 100%); }
  .photo--island-kitchen { left: 591px; top: 214px; width: 319px; height: 292px;
    background: linear-gradient(180deg, #f3f3f2 0%, #dcd9d4 45%, #6b3c29 75%, #3d2418 100%); }
  .photo--dark-kitchen { left: 915px; top: 315px; width: 241px; height: 191px;
    background: linear-gradient(180deg, #e9e4dc 0%, #3d2b22 45%, #d8d2c8 100%); }

  .mission {
    position: absolute; left: 0; top: 509px; width: 1156px; height: 30px;
    background: var(--band);
    font-family: "Cinzel", serif; font-weight: 700; font-size: 19.5px;
    color: var(--white); text-align: center; line-height: 30px; letter-spacing: .3px;
  }

  .column-heading {
    position: absolute;
    font-family: "Cinzel", serif; font-weight: 600; font-size: 20px;
    line-height: 20px; color: var(--heading);
  }
  .service-list {
    position: absolute; list-style: none;
    font-family: "Encode Sans Condensed", sans-serif; font-size: 14.5px;
    line-height: 20px; color: var(--body-text); text-transform: uppercase;
  }
  .service-list li { position: relative; padding-left: 10px; margin-bottom: 8px; }
  .service-list li::before { content: "•"; position: absolute; left: 0; }
  .column-rule { position: absolute; top: 590px; width: 1px; height: 250px; background: var(--rule); }
</style>
</head>
<body>
  <div class="board-label">Inside</div>

  <section class="spread">
    <div class="photo photo--villa" role="img" aria-label="Mediterranean-style home with arched wooden front door and carriage garage door"></div>
    <div class="photo photo--pergola" role="img" aria-label="Outdoor kitchen with stone counters under a wooden pergola"></div>
    <div class="photo photo--shower" role="img" aria-label="Tiled walk-in shower with glass door and lit niche"></div>
    <div class="photo photo--cherry-kitchen" role="img" aria-label="Kitchen with cherry wood cabinets and granite island"></div>
    <div class="photo photo--white-kitchen" role="img" aria-label="White kitchen with range hood and stainless range"></div>
    <div class="photo photo--island-kitchen" role="img" aria-label="White kitchen with wood island, pendant lights and bar stools"></div>
    <div class="photo photo--dark-kitchen" role="img" aria-label="Dark wood kitchen with white island and pendant lights"></div>

    <div class="mission">Our mission is to build every project as if we were building it for ourselves.</div>

    <h2 class="column-heading" style="left:35px; top:578px;">Construction<br>Consulting Services</h2>
    <ul class="service-list" style="left:38px; top:626px;">
      <li>Consultation &amp;<br>Needs Assessment</li>
      <li>Vendor Referrals</li>
      <li>Bid Process &amp; Review</li>
      <li>Design Services</li>
      <li>Design Review/<br>Cost Analysis</li>
    </ul>

    <div class="column-rule" style="left:298px;"></div>

    <h2 class="column-heading" style="left:336px; top:578px;">Types of<br>Construction Projects</h2>
    <ul class="service-list" style="left:339px; top:626px;">
      <li>Full Home Remodels</li>
      <li>Kitchen Remodels</li>
      <li>Bathroom Remodels</li>
      <li>Residential<br>Construction</li>
      <li>Site Improvements</li>
      <li>Swimming Pools</li>
      <li>Tenant Improvements</li>
    </ul>
    <ul class="service-list" style="left:546px; top:626px;">
      <li>Additions</li>
      <li>Commercial<br>Buildings</li>
      <li>Commercial<br>Construction</li>
      <li>Custom Homes</li>
      <li>Outdoor<br>Entertainment</li>
      <li>Patios</li>
    </ul>

    <div class="column-rule" style="left:720px;"></div>

    <h2 class="column-heading" style="left:763px; top:578px;">Construction<br>Capabilities</h2>
    <ul class="service-list" style="left:767px; top:626px;">
      <li>Roofing</li>
      <li>Millwork</li>
      <li>Finish Work</li>
      <li>Hard Wood Flooring</li>
      <li>Tile Work</li>
      <li>Window Installation</li>
      <li>Exterior Door<br>Installations</li>
      <li>Painting</li>
    </ul>
    <ul class="service-list" style="left:970px; top:626px;">
      <li>Landscaping</li>
      <li>Wall Finishes -<br>Interior &amp; Exterior</li>
      <li>Demolition</li>
      <li>Foundations</li>
      <li>Framing</li>
      <li>Plumbing</li>
      <li>Electrical</li>
    </ul>
  </section>
</body>
</html>
```